Meditations CD Cover
Zielgruppe
Wir unterstützen Therapeuten ihre Praxis aufzubauen.
Aufgabenstellung
Ich wünsche einen CD Cover mit Rückseite und CD Druck, wo nicht zu esoterisch aussieht. Bitte keine Buddha, Steine, Yoga, Lotusblume!
ich hätte gerne mein Bild im Vordergrund, nicht zu prominent, klar strukturiert und nicht zu schwer, lieber mehr Platz lassen.
ich hätte gerne eine CD Jewel Cases.
Bitte eine ganz neutralle CD ohne das Grün von der Website. (sonnen-kern-werk.ch)
Die Meditation ist eine Mischung zwischen Business und Meditation, es geht um Kundenfindung.
Etwas schlichtes und modernes.
Was rauf muss:
CD Cover
Mirela Gantenbein-Rusch
Mein Foto
Titel:
Finde Deinen Kompass, Pfad der Stille!
bitte auch schreiben: die ÜBUNGS-CD zum Buch
Logo und mein Bild, nicht zu prominent!!!!
Beispiel: http://lunavertomiel.com/
http://www.bildquello.com/vector/electric-bulb-16125607?st=0561491
http://www.bildquello.com/vector/dart-board-16126309?st=425cf59
http://klangwiese-audio.com/tarnow-lukas-neue-pfade-zu-glueck-ruhe-und-freude-cd
Rückseite:
mein Foto und der Text:
Gehen Sie in die Resonanz und finden Sie den richtigen Klienten.
Gerne unterstütze ich Sie auf diesem wundervollen Weg ...
Mein Name ist Mirela Gantenbein, ich bin erfolgreiche Unternehmerin, die zugleich spiri- tuell denkt und handelt. Und ich bin fest davon überzeugt. Es gibt eine innere Kraft, die nicht nur Berge versetzt. Sondern auch Ihre Praxis fullt.
Auf dieser CD werden Sie angeleitet sich mit ihrem Idealkunden zu treffen. Sie werden entdecken welche Probleme oder Herausforderungen, Wünsche und Ziele Ihr potenzieller Klient.
Vielen Dank und viel Spass :-)

```html
<!DOCTYPE html>
<html lang="de">
<head>
<meta charset="utf-8">
<title>Finde Deinen Kompass – Übungs-CD</title>
<link href="https://fonts.googleapis.com/css2?family=Arizonia&family=Didact+Gothic&family=Mulish:wght@800&display=swap" rel="stylesheet">
<style>
  :root {
    --paper: #ffffff;
    --ink: #1a1410;
    --ink-soft: #3b3129;
    --veil: rgba(255, 246, 236, 0.78);
    --gold-light: #fff2b8;
    --gold: #f2b33a;
    --amber: #c9731f;
    --bronze: #6b4a35;
    --dusk: #3d3a55;
    --photo-light: #e6e6e6;
    --photo-dark: #6e6e6e;
    --logo: #5a5a5a;
    --dot: #d9568a;
  }
  * { box-sizing: border-box; margin: 0; padding: 0; }
  html, body { width: 1200px; height: 370px; overflow: hidden; background: var(--paper); }
  .canvas { position: relative; width: 1200px; height: 370px; }

  .swirl {
    position: absolute;
    background:
      radial-gradient(circle at 55% 45%, var(--gold-light) 0%, var(--gold) 22%, var(--amber) 45%, var(--bronze) 70%, var(--dusk) 100%);
  }

  /* Back insert */
  .back { position: absolute; left: 31px; top: 0; width: 444px; height: 341px; background: var(--paper); box-shadow: 2px 2px 3px rgba(0,0,0,.35); }
  .back .swirl { left: 23px; top: 0; width: 400px; height: 341px; }
  .spine { position: absolute; top: 0; height: 341px; display: flex; align-items: center; justify-content: center; }
  .spine span { font: 700 8px "Mulish", sans-serif; color: var(--ink); white-space: nowrap; }
  .spine--left { left: 0; width: 23px; }
  .spine--left span { transform: rotate(-90deg); }
  .spine--right { right: 0; width: 21px; }
  .spine--right span { transform: rotate(90deg); }

  .back__panel { position: absolute; left: 38px; top: 0; width: 212px; height: 341px; background: var(--veil); }
  .back__text { position: absolute; left: 52px; top: 36px; width: 200px; font: 400 9.4px/11.5px "Didact Gothic", sans-serif; color: var(--ink-soft); }
  .back__text p { margin-bottom: 11px; }
  .back__signature { position: absolute; left: 52px; top: 275px; font: 400 13px "Arizonia", cursive; color: var(--ink); }
  .back__portrait { position: absolute; left: 257px; top: 158px; width: 163px; height: 183px;
    background: linear-gradient(160deg, var(--photo-dark) 0%, var(--photo-light) 60%, var(--paper) 100%); }

  .brand { position: absolute; display: flex; align-items: center; gap: 4px; font: 400 15px "Didact Gothic", sans-serif; color: var(--logo); letter-spacing: .5px; }
  .brand__dot { width: 18px; height: 18px; border-radius: 50%; background: var(--dot); opacity: .8; }
  .back .brand { left: 52px; top: 306px; }

  /* Front cover */
  .front { position: absolute; left: 493px; top: 0; width: 342px; height: 342px; box-shadow: 2px 2px 3px rgba(0,0,0,.35); }
  .front .swirl { inset: 0; }
  .front__band { position: absolute; left: 0; top: 71px; width: 342px; height: 199px; background: var(--veil); }
  .front__title { position: absolute; left: 0; top: 80px; width: 342px; text-align: center; font: 400 26px/33px "Arizonia", cursive; color: var(--ink); }
  .front__author { position: absolute; left: 0; top: 156px; width: 342px; text-align: center; font: 400 18px "Arizonia", cursive; color: var(--ink); }
  .front .brand { left: 36px; top: 228px; }
  .front__tagline { position: absolute; left: 188px; top: 212px; width: 140px; text-align: center; transform: rotate(-6deg);
    font: 800 15px/20px "Mulish", sans-serif; color: var(--ink); }

  /* Disc */
  .disc { position: absolute; left: 854px; top: 16px; width: 332px; height: 332px; border-radius: 50%; overflow: hidden; }
  .disc .swirl { inset: 0; border-radius: 50%; }
  .disc__band { position: absolute; left: 0; top: 140px; width: 332px; height: 53px; background: var(--veil); }
  .disc__title { position: absolute; left: 4px; top: 150px; width: 128px; text-align: center; font: 400 10px/13px "Arizonia", cursive; color: var(--ink); }
  .disc__author { position: absolute; left: 212px; top: 160px; width: 116px; text-align: center; font: 400 10px "Arizonia", cursive; color: var(--ink); }
  .disc__hole { position: absolute; left: 136px; top: 136px; width: 60px; height: 60px; border-radius: 50%; background: var(--paper); }
</style>
</head>
<body>
<div class="canvas">

  <section class="back">
    <div class="swirl" role="img" aria-label="Goldener, orange-brauner Wasserstrudel als Hintergrundbild"></div>
    <div class="spine spine--left"><span>Mirela Gantenbein-Rusch</span></div>
    <div class="spine spine--right"><span>Mirela Gantenbein-Rusch</span></div>
    <div class="back__panel"></div>
    <div class="back__portrait" role="img" aria-label="Schwarzweiss-Porträtfoto der Autorin"></div>
    <div class="back__text">
      <p>Gehen Sie in die Resonanz und<br>finden Sie den richtigen Klienten.<br>Gerne unterstütze ich Sie auf<br>diesem wundervollen Weg.</p>
      <p>Mein Name ist Mirela Gantenbein, ich<br>bin erfolgreiche Unternehmerin, die<br>zugleich spirituell denkt und handelt.<br>Und ich bin fest davon überzeugt.<br>Es gibt eine innere Kraft, die nicht<br>nur Berge versetzt. Sondern auch<br>Ihre Praxis füllt.</p>
      <p>Auf dieser CD werden Sie angeleitet<br>sich mit ihrem Idealkunden zu treffen.<br>Sie werden entdecken welche Probleme<br>oder Herausforderungen, Wünsche und<br>Ziele Ihr potenzieller Klient.</p>
      <p>Vielen Dank und viel Spass</p>
    </div>
    <div class="back__signature">Mirela Gantenbein-Rusch</div>
    <div class="brand"><span class="brand__dot"></span>MGR</div>
  </section>

  <section class="front">
    <div class="swirl" role="img" aria-label="Goldener, orange-brauner Wasserstrudel als Hintergrundbild"></div>
    <div class="front__band"></div>
    <h1 class="front__title">Finde Deinen Kompass,<br>Pfad der Stille!</h1>
    <div class="front__author">Mirela Gantenbein-Rusch</div>
    <div class="brand"><span class="brand__dot"></span>MGR</div>
    <div class="front__tagline">die ÜBUNGS-CD<br>zum Buch</div>
  </section>

  <section class="disc">
    <div class="swirl" role="img" aria-label="Goldener Wasserstrudel als Hintergrundbild der CD"></div>
    <div class="disc__band"></div>
    <div class="disc__title">Finde Deinen Kompass,<br>Pfad der Stille!</div>
    <div class="disc__author">Mirela Gantenbein-Rusch</div>
    <div class="disc__hole"></div>
  </section>

</div>
</body>
</html>
```